New web Design for Velmix

Need a web design for our company Velmix, Inc. We are an IT services company providing our services to State/Local governments, federal government and commercial clients. Please take a look at our existing website (www.velmix-web.com) to know more about our offerings and services. Our website should reflect our services that we provide primarily to state/local and federal governments in the USA and the website should be a responsive and compatible to view it over the web from a PC, tablet or a smart phone with the ability of a CMS.

Reason: We are currently reviewing additional designs. Please submit more asap. Thank you for all your help

Reason: Looking for more design

Reason: Looking for more designs

```html
<!DOCTYPE html>
<html lang="en">
<head>
<meta charset="utf-8">
<title>Velmix – Empowering Government</title>
<link href="https://fonts.googleapis.com/css2?family=Open+Sans:wght@400;600;700&family=Ubuntu:wght@400;500&display=swap" rel="stylesheet">
<style>
:root{
  --navy:#13215a;
  --navy-deep:#0c1640;
  --blue:#1170c9;
  --red:#d8352b;
  --text:#333;
  --muted:#8a8a8a;
  --line:#dcdfe4;
  --footer:#1e1e1e;
  --footer-bar:#141414;
  --footer-text:#6f6f6f;
}
*{box-sizing:border-box;margin:0;padding:0}
html,body{width:1200px;height:2206px;overflow:hidden;background:#fff}
body{font-family:"Open Sans",sans-serif;color:var(--text);position:relative}
.abs{position:absolute}
h2,h3,h4{font-family:"Ubuntu",sans-serif;font-weight:400}

/* header */
.site-header{left:0;top:0;width:1200px;height:121px;background:radial-gradient(circle at 170px 60px,#2d3f8c 0,var(--navy) 160px,var(--navy-deep) 100%)}
.brand{left:98px;top:34px}
.brand-name{font-size:32px;font-weight:700;color:#fff;display:flex;align-items:center;gap:8px;line-height:1}
.brand-name i{display:inline-block;width:14px;height:14px;background:var(--red)}
.brand-tag{font-size:12px;color:#6fb3ff;margin-top:6px}
.search{left:891px;top:44px;width:207px;height:35px;background:#fff;border:1px solid #ccc;display:flex;align-items:center;justify-content:space-between;padding:0 10px;font-size:13px;color:#555}

/* nav */
.main-nav{left:0;top:121px;width:1200px;height:55px;background:var(--blue)}
.main-nav a{position:absolute;top:19px;color:#fff;text-decoration:none;font-size:12px;font-weight:600;white-space:nowrap}

/* hero */
.hero{left:0;top:176px;width:1200px;height:515px;background:linear-gradient(180deg,#7ea8d6 0%,#b9d0e6 40%,#e8ecef 58%,#c9cfd3 68%,#5c7a3a 78%,#4b6d2e 100%)}
.hero-arrow{top:395px}
.dots{left:584px;top:652px;display:flex;gap:7px}
.dots span{width:12px;height:12px;border-radius:50%;background:#fff;border:2px solid #ccc}
.dots span:first-child{background:var(--red);border-color:#fff}

/* services */
.service{top:728px;width:230px;text-align:center}
.service svg{display:block;margin:0 auto}
.service h3{font-size:22px;color:var(--navy);margin-top:14px;white-space:nowrap}
.service p{font-size:11.5px;color:var(--muted);line-height:21px;margin-top:6px}
.service a{display:block;color:var(--red);font-size:12px;margin-top:6px;text-decoration:none}

/* welcome */
.welcome-title{left:98px;top:953px;font-size:25px;color:var(--navy)}
.welcome-title span,.section-title span{color:var(--red)}
.welcome-text{left:98px;top:993px;width:625px;font-size:11.6px;line-height:24px;color:#444}
.team-photo{left:750px;top:966px;width:350px;height:200px;background:linear-gradient(135deg,#e4eef6,#b7c9dc 50%,#8aa1b8)}

.section-title{left:98px;top:1203px;font-size:25px;color:var(--navy)}
.tile{top:1247px;width:316px;height:190px}
.tile span{position:absolute;left:0;bottom:0;width:100%;padding:8px 10px;background:rgba(20,30,60,.55);color:#fff;font-size:14px;font-weight:600}
.tile-state{left:100px;background:linear-gradient(180deg,#2b5aa8,#6e93c9 55%,#c9cdd0)}
.tile-federal{left:441px;background:linear-gradient(180deg,#5d82bd,#b7c4d3 55%,#e5e3dc)}

.solutions{left:818px;top:1213px;width:280px;height:233px;border-radius:10px;background:linear-gradient(180deg,#2f4c93 0,#1c2f70 30%,#0d1a4a 100%);color:#fff;padding:20px 30px}
.solutions h4{font-size:18px;margin-bottom:28px}
.solutions li{list-style:none;font-size:13.5px;line-height:28px;padding-left:14px;position:relative}
.solutions li:before{content:"";position:absolute;left:0;top:10px;border-left:5px solid #fff;border-top:4px solid transparent;border-bottom:4px solid transparent}

.label{left:98px;font-size:21px;font-weight:600;color:var(--navy)}

/* certification badges */
.cert-row{left:114px;top:1537px;width:976px;height:66px;display:flex;justify-content:space-between;align-items:center}
.badge{height:64px;border:1px solid var(--line);background:#fff;display:flex;align-items:center;justify-content:center;padding:8px}
.badge b{display:block;width:100%;height:100%}
.badge .ring{width:44px;height:44px;border-radius:50%}

/* clients */
.client-row{left:100px;top:1702px;width:1000px;height:42px;display:flex;justify-content:space-between;align-items:center}
.client{display:flex;align-items:center;gap:6px;font-size:12px;font-weight:700;color:var(--navy);white-space:nowrap}
.client i{display:inline-block;width:14px;height:14px;flex:none}
.client i.round{border-radius:50%}

/* footer */
.site-footer{left:0;top:1818px;width:1200px;height:319px;background:var(--footer)}
.fcol{top:1850px}
.fcol h4{color:var(--red);font-size:18px;margin-bottom:18px}
.post{font-size:11.5px;font-weight:700;color:var(--footer-text);line-height:15px;width:210px;padding:0 5px 18px;border-bottom:1px solid #333;margin-bottom:18px}
.tweet{width:260px;padding-bottom:8px;border-bottom:1px solid #333;margin-bottom:10px;position:relative;padding-left:25px}
.tweet:before{content:"";position:absolute;left:0;top:3px;width:12px;height:12px;border-radius:50%;background:#fff}
.tweet p{font-size:11px;color:var(--footer-text);line-height:15px}
.tweet p em{font-style:normal;color:var(--red)}
.tweet small{display:block;font-size:10.5px;color:#fff;margin-top:8px}
.field{width:194px;height:28px;background:#fff;margin-bottom:8px;font-size:10.5px;color:#777;padding:7px 10px}
.field.big{height:62px}
.send{display:inline-block;background:var(--red);color:#fff;font-size:12px;font-weight:700;padding:4px 14px;margin-top:2px}
.footer-bar{left:0;top:2137px;width:1200px;height:69px;background:var(--footer-bar);color:#fff;font-size:12.5px;padding:27px 98px}
.social{top:2156px;display:flex;gap:4px;left:965px}
.social span{width:31px;height:31px}
</style>
</head>
<body>

<header class="site-header abs">
  <div class="brand abs">
    <div class="brand-name"><i></i>Velmix</div>
    <div class="brand-tag">Empowering Government</div>
  </div>
  <div class="search abs">Search
    <svg width="18" height="18" viewBox="0 0 18 18"><circle cx="7" cy="7" r="5.5" fill="none" stroke="#111" stroke-width="2.2"/><path d="M11 11l5 5" stroke="#111" stroke-width="2.6"/></svg>
  </div>
</header>

<nav class="main-nav abs">
  <a style="left:142px">Home</a>
  <a style="left:242px">About Us</a>
  <a style="left:360px">Aliances</a>
  <a style="left:474px">Solutions</a>
  <a style="left:592px">Clinets</a>
  <a style="left:698px">Contract Vehicles</a>
  <a style="left:864px">Careers</a>
  <a style="left:974px">Contact Us</a>
</nav>

<section class="hero abs" role="img" aria-label="Photograph of the domed capitol building on a sunny day with lawns and trees"></section>
<svg class="hero-arrow abs" style="left:52px" width="22" height="36" viewBox="0 0 22 36"><path d="M18 3L5 18l13 15" fill="none" stroke="#fff" stroke-width="6"/></svg>
<svg class="hero-arrow abs" style="left:1126px" width="22" height="36" viewBox="0 0 22 36"><path d="M4 3l13 15L4 33" fill="none" stroke="#fff" stroke-width="6"/></svg>
<div class="dots abs"><span></span><span></span><span></span></div>

<div class="service abs" style="left:101px">
  <svg width="66" height="52" viewBox="0 0 66 52"><rect x="3" y="3" width="60" height="46" rx="4" fill="none" stroke="#d8352b" stroke-width="4"/><rect x="18" y="28" width="5" height="11" fill="#d8352b"/><rect x="26" y="23" width="5" height="16" fill="#d8352b"/><rect x="34" y="18" width="5" height="21" fill="#d8352b"/><rect x="42" y="12" width="5" height="27" fill="#d8352b"/></svg>
  <h3>IT Planning</h3>
  <p>Praesent sit amet est In dictum dolor<br>eu dictum porttitor enim felis</p>
  <a>LEARN MORE</a>
</div>
<div class="service abs" style="left:356px">
  <svg width="60" height="52" viewBox="0 0 60 52"><rect x="3" y="3" width="54" height="36" rx="2" fill="none" stroke="#d8352b" stroke-width="4"/><path d="M22 48h16M30 39v9" stroke="#d8352b" stroke-width="4"/><circle cx="26" cy="24" r="5" fill="none" stroke="#d8352b" stroke-width="3"/><circle cx="35" cy="16" r="4" fill="none" stroke="#d8352b" stroke-width="3"/></svg>
  <h3>Systems Integration</h3>
  <p>Praesent sit amet est In dictum dolor<br>eu dictum porttitor enim felis</p>
  <a>LEARN MORE</a>
</div>
<div class="service abs" style="left:610px">
  <svg width="60" height="60" viewBox="0 0 60 60"><circle cx="30" cy="30" r="21" fill="none" stroke="#d8352b" stroke-width="4" stroke-dasharray="10 6"/><rect x="24" y="2" width="12" height="10" fill="#d8352b"/><rect x="24" y="48" width="12" height="10" fill="#d8352b"/><rect x="2" y="24" width="10" height="12" fill="#d8352b"/><rect x="48" y="24" width="10" height="12" fill="#d8352b"/></svg>
  <h3 style="margin-top:6px">Network Services</h3>
  <p>Praesent sit amet est In dictum dolor<br>eu dictum porttitor enim felis</p>
  <a>LEARN MORE</a>
</div>
<div class="service abs" style="left:875px">
  <svg width="60" height="56" viewBox="0 0 60 56"><ellipse cx="24" cy="9" rx="20" ry="7" fill="#d8352b"/><path d="M4 14v9c0 4 9 7 20 7s20-3 20-7v-9c0 4-9 7-20 7S4 18 4 14zM4 28v9c0 4 9 7 20 7v-9C13 35 4 32 4 28z" fill="#d8352b"/><path d="M44 30l12 4v8c0 7-6 11-12 13-6-2-12-6-12-13v-8z" fill="#d8352b" stroke="#fff" stroke-width="2"/></svg>
  <h3 style="margin-top:10px">Data Management</h3>
  <p>Praesent sit amet est In dictum dolor<br>eu dictum porttitor enim felis</p>
  <a>LEARN MORE</a>
</div>

<h2 class="welcome-title abs"><span>Welcome To</span> Velmix</h2>
<p class="welcome-text abs">Lorem ipsum dolor sit amet, consectetuer adipiscing elit, sed diam nonummy nibh euismod tincidunt ut laoreet dolore magna aliquam erat volutpat. Ut wisi enim ad minim veniam, quis nostrud exerci tation ullamcorper suscipit lobortis nisl ut aliquip ex ea commodo consequat. Lorem ipsum dolor sit amet, consectetuer adipiscing elit, sed diam nonummy nibh euismod tincidunt ut laoreet dolore magna aliquam erat volutpat. Ut wisi enim ad minim veniam, quis nostrud exerci tation ullamcorper suscipit lobortis nisl ut aliquip ex ea commodo consequat. Lorem ipsum dolor sit amet, consectetuer adipiscing elit, sed diam nonummy nibh euismod tincidunt ut laoreet dolore</p>
<div class="team-photo abs" role="img" aria-label="Photograph of a team of colleagues collaborating around a laptop"></div>

<h2 class="section-title abs"><span>IT</span> Services</h2>
<div class="tile tile-state abs" role="img" aria-label="Photograph of a capitol dome with a flag"><span>State/Local governments</span></div>
<div class="tile tile-federal abs" role="img" aria-label="Photograph of a columned federal building facade"><span>Federal Government</span></div>

<aside class="solutions abs">
  <h4>Solutions</h4>
  <ul>
    <li>IT Planning</li>
    <li>Mangement Consulting</li>
    <li>Application Development</li>
    <li>Network services</li>
    <li>Web services</li>
  </ul>
</aside>

<h3 class="label abs" style="top:1484px">Certification</h3>
<div class="cert-row abs">
  <div class="badge" style="width:152px"><b style="background:#e8eef8;border:2px solid #2a4f8f"></b></div>
  <div class="badge" style="width:132px"><b style="background:#2b2b2b"></b></div>
  <div class="badge" style="width:120px"><span class="ring" style="background:#1f3f7a"></span></div>
  <div class="badge" style="width:78px"><b style="background:#efe2b8;border:2px solid #d5bf7d"></b></div>
  <div class="badge" style="width:104px"><b style="background:#0d4c8c"></b></div>
  <div class="badge" style="width:112px"><b style="background:#e3cdb4"></b></div>
</div>

<h3 class="label abs" style="top:1646px">Clients</h3>
<div class="client-row abs">
  <div class="client"><i style="background:#0f9a4a"></i>Harbor County</div>
  <div class="client"><i style="background:#1f4f9c"></i>Bayfront Transit</div>
  <div class="client"><i style="background:#2c4a2c"></i>Pinecrest Sheriff</div>
  <div class="client"><i class="round" style="background:#1a7b3a"></i>Greenway Roads</div>
  <div class="client"><i style="background:#3a4f8f"></i>Elmwood County</div>
  <div class="client"><i style="background:#4a8b8e"></i>Lakeview Parks</div>
  <div class="client"><i style="background:#3a3fa0"></i>Metro Valley</div>
  <div class="client"><i class="round" style="background:#222"></i>Ridgeline State</div>
  <div class="client"><i style="background:#222"></i>Cityline IT</div>
</div>

<footer class="site-footer abs"></footer>
<div class="fcol abs" style="left:98px">
  <h4>Recent Post</h4>
  <p class="post">Lid est laborum dolo rumes fuga untras Etharums ser quidem rerum faci</p>
  <p class="post">Lid est laborum dolo rumes fuga untras Etharums ser quidem rerum faci</p>
  <p class="post" style="border:0">Lid est laborum dolo rumes fuga untras Etharums ser quidem rerum faci</p>
</div>
<div class="fcol abs" style="left:356px">
  <h4>Latest Tweets</h4>
  <div class="tweet"><p><em>Chirper Name:</em> The connection to chirper has returned an error. Please try again later.</p><small>◷ about 15 hours ago &nbsp;&nbsp; ◉ Open tweet</small></div>
  <div class="tweet"><p><em>Chirper Name:</em> The connection to chirper has returned an error. Please try again later.</p><small>◷ about 15 hours ago &nbsp;&nbsp; ◉ Open tweet</small></div>
  <div class="tweet" style="border:0"><p><em>Chirper Name:</em> The connection to chirper has returned an error. Please try again later.</p><small>◷ about 15 hours ago &nbsp;&nbsp; ◉ Open tweet</small></div>
</div>
<div class="fcol abs" style="left:675px">
  <h4>What We Do</h4>
  <p class="post" style="width:160px;border:0">Lid est laborum dolo rumes fuga untras Etharums ser quidem rerum faci</p>
</div>
<div class="fcol abs" style="left:901px">
  <h4>Sign Up</h4>
  <div class="field">Name</div>
  <div class="field">Phone</div>
  <div class="field">Email</div>
  <div class="field big">Message</div>
  <span class="send">Send</span>
</div>

<div class="footer-bar abs">© 2014 Velmix - All rights reserved.</div>
<div class="social abs">
  <span style="background:#3b5998"></span>
  <span style="background:#1da1f2"></span>
  <span style="background:#dd4b39"></span>
  <span style="background:#0e76a8"></span>
</div>

</body>
</html>
```